Plofzon car advertisement

de website moet uit minimaal 3 pagina's bestaan. 1 pagina als een landingspagina. 1 pagina voor consumenten die hun auto willen laten beplakken met bedrijfsreclame en 1 pagina voor bedrijven / consumenten die hun bedrijfsreclame op een consumentenauto wilt plaatsen.

de website moet echt een happy website zijn. consumenten kunnen geld verdienen met reclame op hun auto te laten zetten en bedrijven kunnen voor een relatief goedkoop bedrag hun bedrijfsreclame op een auto laten zetten. die auto rijdt dan rond en veel mensen zien de reclame.

beide pagina's moeten dus een glimlach opleveren.

het doel van de startpagina is dat je door kunt gaan naar de consumenten en de bedrijfspagina.

gebruik leuke, vrolijke kleuren en vormen en zorg dat de mensen een glimlach krijgen als ze naar de website kijken.

doelgroep is consumenten die een auto rijden en geld willen verdienen met hun auto en de zakelijke ondernemer die voor een goedkoop bedrag zijn bedrijfsreclame met een full carwrap kan laten zien aan de buitenwereld.

doordat consumenten zich bij ons aanmelden hebben wij een database met auto's en weten we hoeveel deze auto's rijden en in welke regio's ze rijden en wat voor auto ze rijden. allemaal hele belangrijke informatie voor een ondernemer die reclame wilt maken op ene specifieke auto type en in een bepaalde regio.

-

website should consist of at least 3 pages. 1 landing page, 1 customer page and 1 business page. landing page let's the visitor choose wether he / she is a customer with a car and wants to allow his car to be fully carwrapped or he / she is a business owner who wants to place his advertisement on a car.

website should be a really happy joyfull website and bring a smile to the visitor. beause the customer can earn money (200 euro / month nett) by allowing advertisements on his car (full car wrap) and the business owner because for a low price he can advertise.

when customers that owns a car register themselves with our website we build a database with cars in specific locations. a business owner wants to advertise his product into a specific region. this is very valuable information.

agreement is 1 year for a customer to have advertisements on his car and for a business to advertise. after that year, the advertisements are safely removed from the car and new advertisement agreements can be made. a business can place advertisements (full carwrap) already for 795 euro's., Details for my new Web Design Project will be added soon. , de website moet uit minimaal 3 pagina's bestaan. 1 pagina als een landingspagina. 1 pagina voor consumenten die hun auto willen laten beplakken met bedrijfsreclame en 1 pagina voor bedrijven / consumenten die hun bedrijfsreclame op een consumentenauto wilt plaatsen.

Target Market(s)

customers who has a car
businesses who want to advertise their business / product on a car

Industry/Entity Type

Business

Requirements
Must have
• website should be playfull, colorfull and a joy to look at and work with. altough functoinality is very limited visitors need to be intrigued to proceed to contact plofzon.
Nice to have
• nice graphics, moving images, a "living" website (not so static)

```html
<!DOCTYPE html>
<html lang="en">
<head>
<meta charset="utf-8">
<title>Plofzon Car</title>
<link href="https://fonts.googleapis.com/css2?family=PT+Sans:wght@400;700&family=Ubuntu:wght@400;500;700&display=swap" rel="stylesheet">
<style>
:root{
  --blue:#1565b0;
  --blue-dark:#0f4f8f;
  --nav:#1a73c6;
  --bar:#1181d6;
  --heading:#1a6fb5;
  --page:#f6f6f6;
  --text:#222;
  --footer:#2c2c2c;
  --orange:#f39a14;
  --field:#f2f2f2;
}
*{box-sizing:border-box;margin:0;padding:0}
html,body{width:886px;height:1200px;overflow:hidden}
body{font-family:"PT Sans",sans-serif;color:var(--text);background:var(--page);position:relative}
.abs{position:absolute}
.top-band{left:0;top:0;width:886px;height:286px;background:linear-gradient(180deg,#1a5fa8,var(--blue))}
.brand{left:92px;top:12px;display:flex;align-items:center;gap:10px;color:#fff;font-family:"Ubuntu",sans-serif;font-weight:500;font-size:19px;letter-spacing:.5px}
.brand-mark{width:30px;height:30px;border-radius:50%;background:#fff}
.account{left:696px;top:22px;display:flex;font-size:12px}
.account a{display:block;height:24px;line-height:24px;padding:0 10px;color:#fff;text-decoration:none;border-radius:3px}
.account .sign-in{background:#222}
.account .sign-up{background:var(--nav);margin-left:2px}
.nav{left:84px;top:55px;width:724px;height:34px;background:var(--nav);display:flex;align-items:center;padding-left:14px;font-size:12.5px;color:#fff}
.nav a{color:#fff;text-decoration:none;margin-right:34px}
.follow{margin-left:auto;display:flex;align-items:center;gap:4px;padding-right:8px}
.follow span{margin-right:4px}
.follow i{width:20px;height:20px;border-radius:50%;background:#fff;display:block}
.hero{left:84px;top:89px;width:724px;height:303px;background:linear-gradient(180deg,#3d4a33 0%,#5c6b4a 35%,#9aa4a8 55%,#6b6b66 100%)}
.arrow{width:58px;height:58px;border-radius:50%;background:#fff;top:209px;box-shadow:0 2px 6px rgba(0,0,0,.25)}
.arrow svg{position:absolute;left:19px;top:17px}
.info-bar{left:84px;top:402px;width:724px;height:68px;background:var(--bar);color:#fff;font-size:10.5px;line-height:14px;padding:14px 0 0 18px}
.info-bar p{width:520px}
.more{left:551px;top:20px;width:157px;height:28px;border:1px solid #5fb0ef;background:var(--nav);border-radius:3px;font-size:14px;line-height:26px;padding-left:20px;color:#fff}
.more svg{position:absolute;right:22px;top:8px}
h1,h2{font-family:"Ubuntu",sans-serif;color:var(--heading);font-weight:500}
.welcome h1{font-size:19px;margin-bottom:9px}
.welcome{left:82px;top:485px;width:428px;font-size:10px;line-height:15.5px}
.welcome p{margin-bottom:10px}
.welcome p.gap{margin-top:17px}
.thumb{width:124px;height:104px;border-radius:3px}
.social{left:85px;top:689px;display:flex;gap:7px}
.social i{display:block;width:25px;height:25px;border-radius:50%;background:var(--nav)}
.rule{left:83px;top:738px;width:725px;height:2px;background:#c9c9c9}
.services-title{left:84px;top:757px;font-size:15.5px}
.service-col{top:800px;font-size:9px;list-style:none}
.service-col li{height:22.6px;position:relative;padding-left:15px}
.service-col li::before{content:"";position:absolute;left:1px;top:3px;width:4px;height:4px;border-right:1.3px solid #222;border-top:1.3px solid #222;transform:rotate(45deg)}
.request{left:601px;top:762px;width:204px;height:230px;background:var(--blue);padding:14px 9px 0}
.request .field{height:21px;background:var(--field);font-size:9.5px;color:#999;padding:4px 8px;margin-bottom:8px}
.request .field.tall{height:52px;margin-bottom:11px}
.request .submit{height:27px;background:linear-gradient(180deg,#fbb030,#ef8a0a);border-radius:3px;color:#fff3d0;font-family:"Ubuntu",sans-serif;font-weight:700;font-size:11px;text-align:center;line-height:27px;margin:0 2px}
.footer{left:0;top:1007px;width:886px;height:193px;background:var(--footer);color:#fff}
.footer h3{font-weight:400;font-size:14.5px;font-family:"Ubuntu",sans-serif}
.about{left:82px;top:22px;width:135px}
.about h3{font-size:16px;margin-bottom:15px}
.about p{font-size:7.8px;line-height:13px}
.testimonials{left:233px;top:24px;width:290px}
.testimonials h3{margin-bottom:14px}
.quote{position:relative;padding-left:24px;font-size:10px;line-height:14px;margin-bottom:16px}
.quote svg{position:absolute;left:5px;top:8px}
.contact{left:540px;top:24px;width:275px}
.contact h3{margin-bottom:14px}
.contact .row{display:flex;align-items:flex-start;font-size:9.5px;margin-bottom:4px}
.contact .row label{width:58px;padding-top:3px}
.contact .input{width:215px;height:17px;background:#fff;border-radius:2px}
.contact .input.tall{height:39px}
.send{left:738px;top:143px;width:76px;height:17px;background:var(--bar);border-radius:2px;font-size:11px;text-align:center;line-height:17px;color:#fff}
</style>
</head>
<body>
<div class="abs top-band"></div>

<div class="abs brand"><span class="brand-mark"></span>PLOFZON CAR</div>
<div class="abs account"><a class="sign-in">Sign in</a><a class="sign-up">Sign up</a></div>

<nav class="abs nav">
  <a>Home</a><a>About Us</a><a>Our Services</a><a>Our News</a><a>Contact Us</a>
  <div class="follow"><span>Follow us:</span><i></i><i></i><i></i><i></i></div>
</nav>

<div class="abs hero" role="img" aria-label="Small hatchback with a colourful full advertising wrap parked in front of green trees"></div>
<div class="abs arrow" style="left:57px"><svg width="18" height="24" viewBox="0 0 18 24"><path d="M13 2 3 12l10 10" fill="none" stroke="#222" stroke-width="2.5"/></svg></div>
<div class="abs arrow" style="left:775px"><svg width="18" height="24" viewBox="0 0 18 24"><path d="M5 2l10 10-10 10" fill="none" stroke="#222" stroke-width="2.5"/></svg></div>

<section class="abs info-bar">
  <p>Lorem ipsum dolor sit ipsum Lorem ipsum dolor sit ipsum Lorem ipsum dolor sit ipsum Lorem ipsum dolor sit ipsum Lorem ipsum dolor sit ipsum Lorem ipsum dolor sit ipsum Lorem ipsum dolor sit ipsum Lorem ipsum dolor sit ipsumLorem ipsum dolor sit ipsum Lorem ipsum.</p>
  <div class="abs more">More information<svg width="8" height="13" viewBox="0 0 8 13"><path d="M1 1l5.5 5.5L1 12" fill="none" stroke="#fff" stroke-width="2"/></svg></div>
</section>

<section class="abs welcome">
  <h1>Welcome to our website</h1>
  <p>Maecenas faucibus mollis interdum. Nullam id dolor id nibh ultricies vehicula ut id elit. Vestibulum id ligula porta felis euismod semper. Praesent commodo cursus magna, vel scelerisque nisl consectetur et. Cum sociis natoque penatibus et magnis dis parturient montes, nascetur ridiculus mus.</p>
  <p>Donec sed odio dui. Morbi leo risus, porta ac consectetur ac, vestibulum at eros. Aenean eu leo quam. Pellentesque ornare sem lacinia quam venenatis vestibulum. Integer posuere erat a ante venenatis dapibus posuere velit aliquet. ellentesque ornare sem lacinia quam venenatis vestibulum.</p>
  <p class="gap">Donec sed odio dui. Morbi leo risus, porta ac consectetur ac, vestibulum at eros. Aenean eu leo quam. Pellentesque ornare sem lacinia quam venenatis vestibulum.</p>
</section>

<div class="abs thumb" style="left:543px;top:506px;background:linear-gradient(135deg,#c9c6c0,#5a6a80 55%,#c94a3a)" role="img" aria-label="Installer applying wrap film to a car door"></div>
<div class="abs thumb" style="left:683px;top:506px;background:linear-gradient(180deg,#8aa0b8,#9a9a9e 55%,#505458)" role="img" aria-label="Front of a wrapped silver hatchback"></div>
<div class="abs thumb" style="left:544px;top:626px;background:linear-gradient(135deg,#3a3a3a,#8a9aa8 50%,#c9d2d8)" role="img" aria-label="Hands smoothing wrap film on a car panel"></div>
<div class="abs thumb" style="left:683px;top:626px;background:linear-gradient(135deg,#3a3a3a,#8a9aa8 50%,#c9d2d8)" role="img" aria-label="Hands smoothing wrap film on a car panel"></div>

<div class="abs social"><i></i><i></i><i></i><i></i></div>
<div class="abs rule"></div>

<h2 class="abs services-title">Our Services:</h2>
<ul class="abs service-col" style="left:92px">
  <li>Cras mattis consectetur</li><li>Purus sit amet fermentum</li><li>Duis mollis, est non co</li><li>Modo luctus, nisi erat portt</li><li>Tor ligula, eget lacinia odio</li><li>Sem nec elit. Maecenas</li><li>Faucibus mollis interdum</li><li>Nulla vitae elit libero</li>
</ul>
<ul class="abs service-col" style="left:268px">
  <li>Cras mattis consectetur</li><li>Purus sit amet fermentum</li><li>Duis mollis, est non co</li><li>Modo luctus, nisi erat portt</li><li>Tor ligula, eget lacinia odio</li><li>Sem nec elit. Maecenas</li><li>Faucibus mollis interdum</li><li>Nulla vitae elit libero</li>
</ul>
<ul class="abs service-col" style="left:442px">
  <li>Cras mattis consectetur</li><li>Purus sit amet fermentum</li><li>Duis mollis, est non co</li><li>Modo luctus, nisi erat portt</li><li>Tor ligula, eget lacinia odio</li><li>Sem nec elit. Maecenas</li><li>Faucibus mollis interdum</li><li>Nulla vitae elit libero</li>
</ul>

<form class="abs request">
  <div class="field">Name</div>
  <div class="field">Email</div>
  <div class="field">Phone</div>
  <div class="field">Cell</div>
  <div class="field tall">Decription</div>
  <div class="submit">SUBMIT YOUR DETAILS</div>
</form>

<footer class="abs footer">
  <div class="abs about">
    <h3>Zonnewiel</h3>
    <p>Nullam quis risus eget urna mollis ornare vel eu leo. Viv amus sagittis lacus vel augue laoreet rutrum faucibus dolor auctor. Praesent com modo cursus magna, vel scelerisque nisl consect etur et. Maecenas sed diam eget risus varius blandit sit</p>
  </div>
  <div class="abs testimonials">
    <h3>Testimonials:</h3>
    <div class="quote"><svg width="6" height="11" viewBox="0 0 6 11"><path d="M1 1l4 4.5L1 10" fill="none" stroke="#fff" stroke-width="1.4"/></svg>Maecenas faucibus mollis interdum. Morbi leo risus, porta ac consectetur ac, vestibulum at eros. Donec sed odio dui.</div>
    <div class="quote"><svg width="6" height="11" viewBox="0 0 6 11"><path d="M1 1l4 4.5L1 10" fill="none" stroke="#fff" stroke-width="1.4"/></svg>Maecenas faucibus mollis interdum. Morbi leo risus, porta ac consectetur ac, vestibulum at eros. Donec sed odio dui.</div>
    <div class="quote"><svg width="6" height="11" viewBox="0 0 6 11"><path d="M1 1l4 4.5L1 10" fill="none" stroke="#fff" stroke-width="1.4"/></svg>Maecenas faucibus mollis interdum. Morbi leo risus, porta ac consectetur ac, vestibulum at eros. Donec sed odio dui.</div>
  </div>
  <div class="abs contact">
    <h3>Contact us:</h3>
    <div class="row"><label>Your name:</label><span class="input"></span></div>
    <div class="row"><label>Your e-mail:</label><span class="input"></span></div>
    <div class="row"><label>Message:</label><span class="input tall"></span></div>
  </div>
  <div class="abs send">Send</div>
</footer>
</body>
</html>
```